Builders Worksite Corflute Outdoor Sign

We are a building company who are just branching out into new construction. How first new build is our own home which was designed by us and a local architect. We are proud and want to create more advertisement around our business.

We need a corflute sign that can staked outside the construction site and can be seen by people passing by.
Updates

Can we please make the company name and logo bigger (Tidewater Ridge Homes) This needs to be the focus. Can we please replace 'Manu' with 'Contact Us on 021-574-3619'

Target Market(s)

Home owners and people wishing to build on lifestyle blocks in New Zealand.

Font styles to use
Sans Serif

Requirements
Must have
• It needs to feature our:
Logo
Company name
Contact name and number - Manu - 0215743619
Landscape NOT portrait.

```html
<!DOCTYPE html>
<html lang="en">
<head>
<meta charset="utf-8">
<title>Tidewater Ridge Homes – Site Sign</title>
<link rel="stylesheet" href="https://fonts.googleapis.com/css2?family=Jost:wght@400&family=Montserrat:wght@700&display=swap">
<style>
  :root {
    --navy: #18212f;
    --paper: #fdfdfd;
    --white: #ffffff;
  }
  html, body {
    margin: 0;
    padding: 0;
    width: 1200px;
    height: 1200px;
    overflow: hidden;
    background: var(--paper);
  }
  .canvas {
    position: relative;
    width: 1200px;
    height: 1200px;
    background: var(--paper);
  }
  .sign {
    position: absolute;
    left: 41px;
    top: 294px;
    width: 1118px;
    height: 646px;
    background: var(--navy);
  }
  .sign__panel {
    position: absolute;
    left: 17px;
    top: 17px;
    right: 17px;
    height: 406px;
    background: var(--paper);
  }
  .corner-mark {
    position: absolute;
    left: 34px;
    top: 40px;
    width: 84px;
    height: 84px;
    border-radius: 50%;
    background: var(--navy);
  }
  .brand {
    position: absolute;
    left: 0;
    right: 0;
    top: 62px;
    text-align: center;
    color: var(--navy);
    font-family: "Jost", sans-serif;
    font-weight: 400;
  }
  .brand__mark {
    display: block;
    width: 104px;
    height: 104px;
    margin: 0 auto 26px;
    border-radius: 50%;
    background: var(--navy);
  }
  .brand__name {
    margin: 0;
    font-size: 64px;
    line-height: 1;
    letter-spacing: 1px;
  }
  .brand__sub {
    margin: 22px 0 0;
    font-size: 34px;
    line-height: 1;
    letter-spacing: 30px;
    padding-left: 30px;
  }
  .contact {
    position: absolute;
    left: 0;
    right: 0;
    top: 423px;
    height: 223px;
    display: flex;
    align-items: center;
    justify-content: center;
    margin: 0;
    color: var(--white);
    font-family: "Montserrat", sans-serif;
    font-weight: 700;
    font-size: 45px;
    letter-spacing: 0.5px;
  }
</style>
</head>
<body>
<div class="canvas">
  <div class="sign">
    <div class="sign__panel">
      <span class="corner-mark"></span>
      <div class="brand">
        <span class="brand__mark"></span>
        <p class="brand__name">TIDEWATER RIDGE</p>
        <p class="brand__sub">HOMES</p>
      </div>
    </div>
    <p class="contact">Contact Us on 021-574-3619</p>
  </div>
</div>
</body>
</html>
```